Upsell Vertical Banner Ad Design For B2B Marketing Agency Vertical 768px × 1180px IS THE SIZE

I need a banner made for my website www.brightlanepromotionhub.biz This banner will be an upsell advertisement for after someone signs up for my monthly program. When they login to their account for the 1st time I will give them the chance to upgrade their account to our annual program with just one click.

this is a page that upsells it currently to give you an idea how we market ourselves:
https://tlpx.pagevault-example.com/page/tlp-annual-upsell

Use this content:

Are You Ready To Commit To Taking Your Business To The Next Level?

Because We're In This For The Long-Haul and Dedicated To Your Success...

Save $300 By Upgrading To An Annual Membership And Pay Only $74/mth

((BUTTON))Yes, Upgrade My Plan Right Now!

*Must prepay the full year at only $898/yr!

Target Market(s)

business owners

Industry/Entity Type

Marketing

Requirements
Must have
• 768px × 1180px IS THE SIZE vertical

Use this content:

Nice to have
• Use this content:

Should not have
• Use this content:

```html
<!DOCTYPE html>
<html lang="en">
<head>
<meta charset="utf-8">
<title>Annual Membership Upgrade Banner</title>
<link rel="stylesheet" href="https://fonts.googleapis.com/css2?family=Montserrat:ital,wght@0,700;0,800;1,400&display=swap">
<style>
  :root {
    --sky: #74bff7;
    --ocean: #0a8de5;
    --deep: #0079dc;
    --white: #ffffff;
    --sun: #fbe07a;
    --ink: #0b0b0b;
    --pink-start: #f9549f;
    --pink-end: #f22fe8;
  }
  html, body {
    margin: 0;
    padding: 0;
    width: 781px;
    height: 1200px;
    overflow: hidden;
    background: var(--sky);
  }
  .banner {
    position: relative;
    width: 768px;
    height: 1180px;
    transform: scale(1.01693, 1.01695);
    transform-origin: 0 0;
    overflow: hidden;
    font-family: "Montserrat", Arial, sans-serif;
    color: var(--white);
  }
  .backdrop {
    position: absolute;
    inset: 0;
  }
  .headline {
    position: absolute;
    left: 107px;
    top: 108px;
    margin: 0;
    font-weight: 800;
    text-transform: uppercase;
    font-size: 60px;
    line-height: 66px;
    letter-spacing: 1px;
  }
  .headline .accent {
    color: var(--sun);
    display: block;
  }
  .headline .accent-big {
    color: var(--sun);
    display: block;
    font-size: 104px;
    line-height: 84px;
    letter-spacing: 7px;
  }
  .headline .accent-big:first-of-type { margin-top: 6px; }
  .subline {
    position: absolute;
    left: 108px;
    top: 574px;
    margin: 0;
    font-weight: 800;
    text-transform: uppercase;
    font-size: 38px;
    line-height: 50px;
    letter-spacing: 0.5px;
  }
  .offer {
    position: absolute;
    left: 80px;
    width: 610px;
    top: 818px;
    margin: 0;
    text-align: center;
    font-weight: 800;
    text-transform: uppercase;
    font-size: 28px;
    line-height: 40px;
    color: var(--ink);
    text-shadow: 3px 2px 0 var(--sun);
    letter-spacing: -0.3px;
  }
  .cta {
    position: absolute;
    left: 218px;
    top: 976px;
    width: 340px;
    height: 90px;
    border-radius: 45px;
    background: linear-gradient(90deg, var(--pink-start), var(--pink-end));
    box-shadow: 0 6px 14px rgba(0, 40, 120, 0.25);
    display: flex;
    align-items: center;
    justify-content: center;
    font-weight: 800;
    font-size: 36px;
    color: var(--white);
    text-decoration: none;
    letter-spacing: 0.5px;
  }
  .fine-print {
    position: absolute;
    left: 0;
    width: 768px;
    top: 1104px;
    margin: 0;
    text-align: center;
    font-style: italic;
    font-weight: 400;
    font-size: 22px;
    text-transform: uppercase;
    letter-spacing: 0.3px;
  }
</style>
</head>
<body>
  <main class="banner">
    <svg class="backdrop" width="768" height="1180" viewBox="0 0 768 1180" aria-hidden="true">
      <rect width="768" height="1180" fill="var(--sky)"/>
      <polygon points="0,360 768,1066 768,1180 0,1180" fill="var(--ocean)"/>
      <polygon points="0,600 62,1180 0,1180" fill="var(--deep)"/>
    </svg>

    <h1 class="headline">
      Are you ready<br>to commit to<br>taking your
      <span class="accent">business to the</span>
      <span class="accent-big">Next</span>
      <span class="accent-big">Level?</span>
    </h1>

    <p class="subline">Because we're in this<br>for the long-haul &amp;<br>dedicated to your<br>success...</p>

    <p class="offer">Save $300 by upgrading to an<br>annual membership and pay<br>only $74/mth</p>

    <a class="cta" href="#upgrade">YES, I’M IN</a>

    <p class="fine-print">*Must prepay the full year at only $898/yr!</p>
  </main>
</body>
</html>
```